Kestrin Supply Website Redesign

Currently kestrinsupply.example is focussed on fulfillment and transport from various products in the BBQ segment. However, no we want to update our business activities to Product Development, Brand Development, Online Positioning, Logistics & Aftersales, and Promotional BBQs. We will be a business for Outdoor Leisure Development from A to Z.

Therefore, we need a brand new website. The colours of the current website may be the same. However, i'd like to keep it clean. More white and use blue and green as accent colours. It is a business to business organization so the website should be looking formal and corporate. However we sell fun products so not too formal and corporate.

Pages we need; Home, About, Contact, Our Services (+ page per service) a place to share our news/blogs.

I have added some sort of mock up of an idea. However it needs some finetuning.

Businesses

Corporate/Logistics/Marketing

Coded - Design and coding required

Designer to choose colors to be used in the design.

• Show clear distinguishing of the different services we provide (Product Development, Brand Development, Online Positioning, Logistics & Aftersales and Promotional BBQs). Every service should have its own page too. Besides, I would like to have a blog page to share relevant content.
• Show that we are the expert in Outdoor LEisure Development from A to Z
• Be too informal. It may be semi-formal

```html
<!DOCTYPE html>
<html lang="en">
<head>
<meta charset="utf-8">
<title>Kestrin Supply — Outdoor Leisure Development</title>
<link href="https://fonts.googleapis.com/css2?family=Mulish:wght@400;600;700;800;900&display=swap" rel="stylesheet">
<style>
:root{
  --green:#3aaa48;
  --slate:#3e6b79;
  --navy:#1b3868;
  --ink:#2b2b2b;
  --text:#555b60;
  --white:#ffffff;
  --ring:#ececec;
}
*{box-sizing:border-box;margin:0;padding:0}
html,body{width:1200px;height:3567px;overflow:hidden}
body{position:relative;font-family:"Mulish",sans-serif;background:var(--white);color:var(--ink)}
.abs{position:absolute}
.disc{position:absolute;border-radius:50%}

/* hero */
.hero{position:absolute;left:0;top:0;width:1200px;height:637px;
  background:linear-gradient(135deg,#3b4a55 0%,#5a4e48 30%,#2f4552 60%,#4b5a52 100%);overflow:hidden}
.hero::after{content:"";position:absolute;inset:0;background:rgba(20,30,40,.35)}
.brand{position:absolute;font-weight:900;color:var(--slate);display:flex;align-items:center;gap:10px;z-index:2;white-space:nowrap}
.brand .dot{border-radius:50%;background:var(--green);flex:none}
.hero .brand{left:72px;top:12px;font-size:34px}
.hero .brand .dot{width:24px;height:24px}
.nav{position:absolute;top:22px;left:0;z-index:2;font-size:16px;font-weight:600;color:var(--white)}
.nav a{position:absolute;color:inherit;text-decoration:none;white-space:nowrap}
.nav a.active{color:var(--green)}
.hero-copy{position:absolute;left:0;width:1200px;text-align:center;color:var(--white);z-index:2}
.hero-kicker{top:218px;font-size:56px;font-weight:400}
.hero-title{top:286px;font-size:98px;font-weight:900;letter-spacing:6px}
.hero-sub{top:400px;font-size:48px;font-weight:900}

/* services */
.section-title{position:absolute;left:0;width:1200px;text-align:center;font-size:50px;font-weight:900;color:var(--ink)}
.service-label{position:absolute;font-size:25px;font-weight:900;color:var(--slate);line-height:29px}
.service-label.right{text-align:right}
.service-label.center{text-align:center}

/* banner */
.banner{position:absolute;left:0;top:1543px;width:1200px;height:415px;
  background:linear-gradient(180deg,#3b5f8c 0%,#1f4a7e 45%,#153a6b 100%)}
.banner h2{position:absolute;top:110px;width:100%;text-align:center;color:var(--white);font-size:57px;font-weight:900}
.banner p{position:absolute;top:196px;left:195px;width:810px;text-align:center;color:var(--white);font-size:23px;line-height:33px;font-weight:600}

/* about */
.about-title{position:absolute;left:613px;top:2070px;font-size:50px;font-weight:900}
.about-text{position:absolute;left:613px;top:2143px;width:520px;font-size:16.5px;line-height:29.5px;color:var(--text)}
.about-text p+p{margin-top:10px}
.btn{position:absolute;background:var(--green);color:var(--white);font-weight:800;border-radius:22px;
  display:flex;align-items:center;justify-content:center;font-size:16px}

/* news */
.card{position:absolute;top:2605px;width:334px;height:332px;background:var(--white);box-shadow:0 0 8px rgba(0,0,0,.18);border:4px solid #fff}
.card .media{width:100%;height:193px}
.card .meta{position:absolute;left:13px;top:212px;font-size:12.5px;color:var(--text)}
.card .meta b{color:var(--navy)}
.card h3{position:absolute;left:13px;top:236px;width:300px;font-size:17px;line-height:25px;font-weight:600;color:var(--ink)}
.card .plus{position:absolute;left:13px;top:295px;width:17px;height:17px;border-radius:50%;background:var(--green);color:#fff;font-size:15px;line-height:17px;text-align:center;font-weight:800}
.card .bar{position:absolute;left:18px;bottom:0;width:224px;height:6px;background:var(--green)}

/* footer */
.footer{position:absolute;left:0;top:3087px;width:1200px;height:480px;
  background:linear-gradient(100deg,#1b2f5e 0%,#1c4677 55%,#175a86 100%);color:var(--white)}
.footer .brand{left:72px;top:88px;font-size:34px;color:var(--white)}
.footer .brand .dot{width:26px;height:26px}
.contact{position:absolute;left:72px;font-size:14px;line-height:19px;display:flex;gap:14px}
.contact svg{flex:none;margin-top:2px}
.col{position:absolute;top:84px}
.col::before{content:"";position:absolute;left:0;top:-30px;width:76px;height:1px;background:var(--green)}
.col h4{font-size:16px;font-weight:600;letter-spacing:.3px;margin-bottom:20px}
.col ul{list-style:none}
.col li{font-size:14.5px;height:27.7px;padding-left:28px;position:relative;white-space:nowrap}
.col li::before{content:"";position:absolute;left:0;top:7px;width:6px;height:6px;border-radius:50%;background:var(--green)}
.col p{font-size:14.5px;line-height:23px;width:260px}
.field{position:absolute;left:879px;top:200px;width:249px;height:43px;background:#fff;color:#333;font-size:13px;display:flex;align-items:center;justify-content:center}
.submit{position:absolute;left:879px;top:249px;width:249px;height:44px;background:var(--green);font-size:13.5px;font-weight:800;display:flex;align-items:center;justify-content:center}
.rule{position:absolute;top:372px;height:1px;background:rgba(255,255,255,.4)}
.social{position:absolute;top:355px;width:34px;height:34px;border-radius:50%;background:#fff}
.copy{position:absolute;top:420px;width:100%;text-align:center;font-size:13px}
</style>
</head>
<body>

<header class="hero">
  <div class="abs" role="img" aria-label="Aerial view of a container port with stacked shipping containers" style="inset:0"></div>
  <div class="brand"><span class="dot"></span>Kestrin Supply</div>
  <nav class="nav">
    <a class="active" style="left:749px">Home</a>
    <a style="left:836px">About</a>
    <a style="left:925px">Our Services</a>
    <a style="left:1066px">Contact</a>
  </nav>
  <div class="hero-copy hero-kicker">Outdoor Leisure</div>
  <div class="hero-copy hero-title">DEVELOPMENT</div>
  <div class="hero-copy hero-sub">From A to Z</div>
</header>

<div class="disc" style="left:-110px;top:455px;width:262px;height:290px;background:var(--green);opacity:.85"></div>
<div class="disc" style="left:1147px;top:590px;width:140px;height:140px;background:var(--slate)"></div>
<div class="disc" style="left:1128px;top:540px;width:100px;height:100px;background:var(--green);opacity:.85"></div>

<h2 class="section-title" style="top:722px">Our Services</h2>
<svg class="abs" style="left:0;top:0" width="1200" height="1500" viewBox="0 0 1200 1500">
  <path d="M440 850 A300 300 0 0 0 331 1058" fill="none" stroke="var(--slate)" stroke-width="4"/>
  <path d="M387 850 A300 300 0 1 0 831 850" fill="none" stroke="var(--slate)" stroke-width="4"/>
  <path d="M785 850 A300 300 0 0 1 887 1058" fill="none" stroke="var(--slate)" stroke-width="4"/>
  <circle cx="609" cy="1052" r="166" fill="var(--green)"/>
  <circle cx="609" cy="1052" r="156" fill="#fff"/>
  <defs><radialGradient id="city" cx="50%" cy="45%" r="60%"><stop offset="0" stop-color="#8fc3ea"/><stop offset=".5" stop-color="#1f5a9a"/><stop offset="1" stop-color="#0d2c5c"/></radialGradient></defs>
  <circle cx="609" cy="1052" r="150" fill="url(#city)" role="img" aria-label="Night city skyline with light trails"/>
  <text x="609" y="1042" text-anchor="middle" font-family="Mulish,sans-serif" font-weight="900" font-size="40" fill="#fff">Kestrin</text>
  <text x="609" y="1088" text-anchor="middle" font-family="Mulish,sans-serif" font-weight="900" font-size="40" fill="#fff">Supply</text>
  <g fill="var(--ring)"><circle cx="329" cy="913" r="76"/><circle cx="893" cy="913" r="76"/><circle cx="329" cy="1160" r="76"/><circle cx="893" cy="1160" r="76"/><circle cx="599" cy="1311" r="76"/></g>
  <g fill="#fff"><circle cx="329" cy="913" r="72"/><circle cx="893" cy="913" r="72"/><circle cx="329" cy="1160" r="72"/><circle cx="893" cy="1160" r="72"/><circle cx="599" cy="1311" r="72"/></g>
  <g fill="var(--green)"><circle cx="329" cy="913" r="66"/><circle cx="893" cy="913" r="66"/><circle cx="329" cy="1160" r="66"/><circle cx="893" cy="1160" r="66"/><circle cx="599" cy="1311" r="66"/></g>
  <g fill="none" stroke="#fff" stroke-width="2.5" stroke-linejoin="round" stroke-linecap="round">
    <path d="M303 912 L329 900 L355 912 L355 942 L329 952 L303 942 Z M303 912 L329 924 L355 912 M329 924 V952"/>
    <circle cx="329" cy="884" r="8"/><path d="M326 893 h6"/>
    <path d="M870 890 L916 936 M916 890 L870 936"/><circle cx="868" cy="938" r="7"/><circle cx="918" cy="888" r="7"/>
    <path d="M308 1150 h30 v24 h-30 z M315 1150 v-10 h16 v10 M300 1180 h42 l12 -8"/><circle cx="350" cy="1140" r="8"/>
    <path d="M868 1140 h34 v42 h-34 z M876 1168 h10"/><path d="M912 1168 c-7 -9 -7 -18 0 -18 c7 0 7 9 0 18 z"/>
    <path d="M578 1322 L608 1296 L622 1330 Z M578 1322 l-6 10 l10 8 l6 -8 M632 1292 l8 -8 M636 1306 h10"/>
  </g>
</svg>
<div class="service-label right" style="left:40px;top:885px;width:190px">Product<br>Development</div>
<div class="service-label" style="left:996px;top:885px">Logistic &amp;<br>Aftersales</div>
<div class="service-label right" style="left:40px;top:1130px;width:190px">Brand<br>Development</div>
<div class="service-label" style="left:981px;top:1138px">Online<br>Positioning</div>
<div class="service-label center" style="left:453px;top:1394px;width:300px">Promotional<br>BBQs</div>

<section class="banner">
  <div class="abs" role="img" aria-label="Blue-toned city skyline at night" style="inset:0"></div>
  <h2>We Make The Differences</h2>
  <p>Many desktop publishing packages and web page editors now use<br>Lorem Ipsum as their default model text, and a search for 'lorem ipsum'<br>will uncover .</p>
</section>
<div class="disc" style="left:1147px;top:1916px;width:140px;height:140px;background:var(--slate)"></div>
<div class="disc" style="left:1128px;top:1856px;width:100px;height:100px;background:var(--green);opacity:.85"></div>

<div class="disc" style="left:67px;top:2007px;width:456px;height:456px;background:#f2f2f2"></div>
<div class="disc" style="left:93px;top:2033px;width:404px;height:404px;background:var(--green)"></div>
<div class="disc" role="img" aria-label="Man working on a laptop in an office" style="left:107px;top:2047px;width:376px;height:376px;background:linear-gradient(160deg,#e8e6e2 0%,#9a968f 55%,#4c4a47 100%)"></div>
<div class="disc" style="left:72px;top:1952px;width:190px;height:190px;background:var(--green);opacity:.85"></div>
<h2 class="about-title">About Us</h2>
<div class="about-text">
  <p>Many desktop publishing packages and web page editors now use Lorem Ipsum as their default model text, and a search for 'lorem ipsum' will uncover many .</p>
  <p>There are many variations of passages of Lorem Ipsum available, but the majority have suffered alteration in some form, by injected humour,</p>
</div>
<div class="btn" style="left:613px;top:2345px;width:130px;height:43px">Read More</div>

<h2 class="section-title" style="top:2515px">Latest News</h2>
<article class="card" style="left:73px">
  <div class="media" role="img" aria-label="Team reviewing app designs on a desk" style="background:linear-gradient(135deg,#d9c8b8,#b99a88 60%,#e4ddd6)"></div>
  <div class="meta"><b>NOV 29,2021</b> / BY LOREM IPSUM</div>
  <h3>Lorem Ipsum is simply dummy text of the printing</h3>
  <div class="plus">+</div><div class="bar"></div>
</article>
<article class="card" style="left:433px">
  <div class="media" role="img" aria-label="Hand pointing at a laptop screen" style="background:linear-gradient(135deg,#6a6d72,#c9c6c2 55%,#8b8d90)"></div>
  <div class="meta"><b>NOV 29,2021</b> / BY LOREM IPSUM</div>
  <h3>Lorem Ipsum is simply dummy text of the printing</h3>
  <div class="plus">+</div><div class="bar"></div>
</article>
<article class="card" style="left:793px">
  <div class="media" role="img" aria-label="Smartphone with a business app on a white desk" style="background:linear-gradient(135deg,#f2f2f2,#e2e2e2 60%,#f6f0e0)"></div>
  <div class="meta"><b>NOV 29,2021</b> / BY LOREM IPSUM</div>
  <h3>Lorem Ipsum is simply dummy text of the printing</h3>
  <div class="plus">+</div><div class="bar"></div>
</article>
<div class="btn" style="left:534px;top:2969px;width:132px;height:43px">View All</div>

<footer class="footer">
  <div class="brand"><span class="dot"></span>Kestrin Supply</div>
  <div class="contact" style="top:168px">
    <svg width="12" height="16" viewBox="0 0 12 16"><path d="M6 0a6 6 0 0 0-6 6c0 4.5 6 10 6 10s6-5.5 6-10a6 6 0 0 0-6-6zm0 8.5A2.5 2.5 0 1 1 6 3.5a2.5 2.5 0 0 1 0 5z" fill="#fff"/></svg>
    <span>Lindeweg 12<br>4811 KT ,Veldhaven,The<br>Netherlands</span>
  </div>
  <div class="contact" style="top:238px">
    <svg width="13" height="13" viewBox="0 0 24 24"><path d="M6.6 10.8a15 15 0 0 0 6.6 6.6l2.2-2.2c.3-.3.7-.4 1-.2 1.1.4 2.3.6 3.6.6.6 0 1 .4 1 1V20c0 .6-.4 1-1 1A17 17 0 0 1 3 4c0-.6.4-1 1-1h3.5c.6 0 1 .4 1 1 0 1.3.2 2.5.6 3.6.1.3 0 .7-.2 1z" fill="#fff"/></svg>
    <span>555-014-2290</span>
  </div>
  <div class="contact" style="top:272px">
    <svg width="12" height="10" viewBox="0 0 12 10" style="margin-top:5px"><rect width="12" height="10" fill="#fff"/><path d="M0 0 L6 5 L12 0" stroke="#1c4677" fill="none"/></svg>
    <span>www.kestrinsupply.example</span>
  </div>

  <div class="col" style="left:415px"><h4>QUICK LINK</h4>
    <ul><li>Home</li><li>About</li><li>Services</li><li>Contact</li><li>Blog</li></ul></div>
  <div class="col" style="left:619px"><h4>SERVICES</h4>
    <ul><li>Product Development</li><li>Brand Development</li><li>Online Positioning</li><li>Logistics &amp; Aftersales</li><li>Promotional BBQs</li></ul></div>
  <div class="col" style="left:876px"><h4>NEWSLETTER</h4>
    <p>Lorem ipsum is placeholder text commonly used in the graphic,</p></div>
  <div class="field">Enter Your Mail ID</div>
  <div class="submit">SUBMIT NOW</div>

  <div class="rule" style="left:152px;width:370px"></div>
  <div class="rule" style="left:680px;width:355px"></div>
  <div class="social" style="left:520px"></div>
  <div class="social" style="left:562px"></div>
  <div class="social" style="left:603px"></div>
  <div class="social" style="left:645px"></div>
  <div class="copy">© 2021 <b>Kestrin Supply.</b> All rights reserved.</div>
</footer>
<div class="disc" style="left:1085px;top:2960px;width:220px;height:240px;background:var(--green);opacity:.85"></div>

</body>
</html>
```